Website for the new investment company.

We are building a website for a new company. This will be an investment company. The name of the company is Tern Harbor Equity, or THE. We don't have a company logo yet, so happy to take suggestions on that as well (and will add that to the final cost). The investors of this company will exclusively be Dunmore College alumni graduates. The investors are not students, but instead older professionals in various industries, that previously graduated from the Dunmore College. This company will establish an investment fund and invest in multiple businesses.
The purpose of the website will be to educate Dunmore alumni on the investment fund.
We are looking for:
1. The design to be relatable, but not the copy of the Dunmore College website. https://www.dunmorecol.edu/
2. This is an investment website and must mimic other similar websites
https://plovergate-fund.com/
https://www.brindlevest.com/
https://kestowholdings.com/site/global/home/p_home.gsp
3. Project timeline. We are focused on receiving a design in the next two weeks and then finishing the website over the following 2 weeks. We anticipate paying for additional work and customization after the designs are provided.
4. Website Pages:
1) Homepage - Mission and Objective (high quality photos along with text that we will provide after selecting the winning design)
2) Background - Text and biographies on the 2 founders (high quality photos along with text that we will provide after selecting the winning design)
3) Advisory Board - Text and biographies on the investment Fund's 3 advisory board members (high quality photos along with text that we will provide after selecting the winning design)
4) Fund I - Text and information on the specific investment fund including pictures and biographies of the investment committee (high quality photos along with text that we will provide after selecting the winning design)
5) Contact Us - Typical website contact page for visitors

Target Market(s)

Dunmore Alumni graduates

Industry/Entity Type

Investment

Coding

Coded - Design and coding required

Font styles to use
Serif
Sans Serif

Colors
0054AA
0677BA
7BADD7
CADEEF
E8F1F8

Requirements
Must have
• Must look like other private investment websites as provided in project description
Nice to have
• Mimics the Dunmore College style, but definitely needs to be different. This company has no direct relationship with Dunmore College.
Should not have
• No commercial transactions, no credit card payments etc. Do not replicate any logos, designs or proprietary content from Dunmore College.

```html
<!DOCTYPE html>
<html lang="en">
<head>
<meta charset="utf-8">
<title>Investment company</title>
<link rel="stylesheet" href="https://fonts.googleapis.com/css2?family=Poppins:wght@500;600;700;800&family=Manrope:wght@400;500&display=swap">
<style>
:root{
  --blue:#0054AA;
  --blue-mid:#0677BA;
  --blue-soft:#7BADD7;
  --blue-pale:#CADEEF;
  --ink:#111;
  --body:#222;
  --white:#fff;
  --rule:#e3e3e3;
}
*{margin:0;padding:0;box-sizing:border-box}
html,body{width:720px;height:1200px;overflow:hidden;background:var(--white)}
body{position:relative;font-family:"Manrope",sans-serif;color:var(--body)}
.hero{position:absolute;left:0;top:0;width:720px;height:370px;overflow:hidden}
.hero-photo{position:absolute;inset:0;background:
  linear-gradient(180deg,#8fb6d2 0%,#c9c7b4 18%,#f0c677 30%,#c99a6a 45%,#8c7d6e 62%,#6f6a5c 80%,#5a5448 100%)}
.brand{position:absolute;left:80px;top:16px;font-family:"Poppins",sans-serif;font-weight:700;font-size:15px;line-height:17px;color:#222}
.main-nav{position:absolute;right:76px;top:20px;display:flex;gap:0;align-items:center}
.main-nav a{font-size:9.5px;font-weight:500;color:#111;text-decoration:none;padding:5px 6px;margin-left:9px;letter-spacing:.1px}
.main-nav a.active{background:var(--blue);color:var(--white);margin-left:0}
.hero-copy{position:absolute;left:0;right:0;top:150px;text-align:center;color:var(--white);font-family:"Poppins",sans-serif;text-shadow:0 1px 3px rgba(0,0,0,.45)}
.hero-copy h1{font-size:27px;font-weight:700;line-height:34px}
.hero-copy p{font-size:12px;font-weight:700;margin-top:4px}
.btn-solid{display:inline-block;margin-top:20px;background:var(--blue);color:var(--white);font-family:"Poppins",sans-serif;font-weight:700;font-size:9px;padding:9px 15px;border:1px solid var(--white);text-decoration:none;text-shadow:none}
.slider-dots{position:absolute;top:336px;left:336px;display:flex;gap:7px}
.slider-dots span{width:7px;height:7px;border-radius:50%;background:var(--white)}
.slider-dots span.on{background:var(--blue);border:1.5px solid var(--white)}
.welcome{position:absolute;top:400px;left:0;width:720px;text-align:center;font-family:"Poppins",sans-serif}
.welcome .kicker{font-size:17px;font-weight:800;color:var(--ink);line-height:20px}
.welcome h2{font-size:23px;font-weight:800;color:var(--blue);line-height:30px;margin-top:3px}
.rule-blue{width:32px;height:2px;background:var(--blue);margin:18px auto 0}
.welcome .intro{font-family:"Manrope",sans-serif;font-size:9px;line-height:14.5px;width:400px;margin:22px auto 0;color:var(--body)}
.values{position:absolute;top:570px;left:80px;width:560px;display:flex}
.value{flex:1;text-align:center;border-left:1px solid var(--rule);height:160px;padding:0 10px}
.value:first-child{border-left:none}
.value svg{width:46px;height:46px;display:block;margin:0 auto}
.value h3{font-family:"Poppins",sans-serif;font-weight:500;font-size:11px;color:var(--ink);margin-top:20px}
.value p{font-size:7.5px;line-height:11.5px;margin-top:10px}
.future{position:absolute;top:769px;left:0;width:720px;height:302px}
.future-panel{position:absolute;left:0;top:0;width:354px;height:302px;background:var(--blue);color:var(--white);padding:30px 0 0 80px}
.future-panel h2{font-family:"Poppins",sans-serif;font-weight:800;font-size:22px;line-height:26px}
.rule-white{width:46px;height:2px;background:var(--white);margin-top:14px}
.future-panel p{font-size:9.2px;line-height:13.5px;width:256px;margin-top:24px}
.btn-outline{display:inline-block;margin-top:22px;margin-left:2px;border:1px solid var(--white);color:var(--white);font-family:"Poppins",sans-serif;font-weight:700;font-size:9px;padding:8px 15px;text-decoration:none}
.future-photo{position:absolute;left:354px;top:0;width:366px;height:302px;background:linear-gradient(135deg,#bfb3a3 0%,#a9b9cf 40%,#8a6a52 75%,#5b4434 100%)}
.site-footer{position:absolute;top:1071px;left:0;width:720px;height:129px;background:linear-gradient(180deg,#0a74b8,#0a6fb2);color:var(--white)}
.footer-brand{position:absolute;left:80px;top:27px;font-family:"Poppins",sans-serif;font-weight:600;font-size:13.5px}
.footer-nav{position:absolute;right:78px;top:32px;display:flex;gap:18px}
.footer-nav a{color:var(--white);font-size:8px;text-decoration:none;font-weight:500}
.footer-rule{position:absolute;left:80px;top:69px;width:560px;height:1px;background:rgba(255,255,255,.7)}
.copyright{position:absolute;top:96px;left:0;width:720px;text-align:center;font-size:8px}
</style>
</head>
<body>
<header class="hero">
  <div class="hero-photo" role="img" aria-label="Aerial photo of a downtown skyline at sunset"></div>
  <div class="brand">Investment<br>company</div>
  <nav class="main-nav">
    <a class="active" href="#">HOME</a><a href="#">ABOUT US</a><a href="#">INVESTMENTS</a><a href="#">INVESTORS</a><a href="#">CONTACT US</a>
  </nav>
  <div class="hero-copy">
    <h1>Empowering Your Financial Future</h1>
    <p>Achieve your investment goals with expert guidance and personalized strategies</p>
    <a class="btn-solid" href="#">READ MORE</a>
  </div>
  <div class="slider-dots"><span class="on"></span><span></span><span></span><span></span></div>
</header>

<section class="welcome">
  <div class="kicker">WELCOME TO</div>
  <h2>INVESTMENT COMPANY</h2>
  <div class="rule-blue"></div>
  <p class="intro">Lorem ipsum dolor sit amet, consectetur adipiscing elit sed do eiusmod tempor incididunt ut labore et dolore magna aliqua. Ut enim ad minim veniam quis nostrud exercitation ullamco laboris &nbsp;nisi ut aliquip ex ea commodo consequat. Duis aute irure dolor in .</p>
</section>

<section class="values">
  <div class="value">
    <svg viewBox="0 0 48 48" fill="none" stroke="#0054AA" stroke-width="1.6" stroke-linejoin="round">
      <circle cx="24" cy="22" r="19"/>
      <circle cx="24" cy="22" r="5"/>
      <path d="M24 11v4M24 29v4M13 22h4M31 22h4M16.2 14.2l2.8 2.8M29 27l2.8 2.8M16.2 29.8l2.8-2.8M29 17l2.8-2.8"/>
    </svg>
    <h3>Intentional</h3>
    <p>Lorem ipsum dolor sit amet, consectetur adipiscing elit sed do eiusmod tempor incididunt ut labore et dolore magna aliqua. Ut enim ad minim v eniam quis nostrud</p>
  </div>
  <div class="value">
    <svg viewBox="0 0 48 48" fill="none" stroke="#0054AA" stroke-width="1.8" stroke-linejoin="round" stroke-linecap="round">
      <path d="M24 4l5 4 6-1 2 6 5 4-2 6 2 6-5 4-2 6-6-1-5 4-5-4-6 1-2-6-5-4 2-6-2-6 5-4 2-6 6 1z"/>
      <path d="M16 25l6 6 11-12"/>
    </svg>
    <h3>Trustworthy</h3>
    <p>Lorem ipsum dolor sit amet, consectetur adipiscing elit sed do eiusmod tempor incididunt ut labore et dolore magna aliqua. Ut enim ad minim v eniam quis nostrud</p>
  </div>
  <div class="value">
    <svg viewBox="0 0 48 48" fill="none" stroke="#0054AA" stroke-width="1.6" stroke-linejoin="round" stroke-linecap="round">
      <path d="M24 3v5M24 40v5M5 24h5M38 24h5M10 10l4 4M34 34l4 4M10 38l4-4M34 14l4-4"/>
      <path d="M17 24a7 7 0 1 1 14 0c0 4-3 5-3 9h-8c0-4-3-5-3-9z"/>
      <path d="M20 36h8M21 39h6"/>
    </svg>
    <h3>Inspiration</h3>
    <p>Lorem ipsum dolor sit amet, consectetur adipiscing elit sed do eiusmod tempor incididunt ut labore et dolore magna aliqua. Ut enim ad minim v eniam quis nostrud</p>
  </div>
  <div class="value">
    <svg viewBox="0 0 48 48" fill="none" stroke="#0054AA" stroke-width="1.6" stroke-linejoin="round">
      <rect x="8" y="8" width="12" height="12"/>
      <rect x="26" y="8" width="12" height="12"/>
      <rect x="8" y="26" width="12" height="12"/>
      <rect x="26" y="26" width="12" height="12"/>
      <path d="M20 14h6M14 20v6M32 20v6M20 32h6"/>
    </svg>
    <h3>Collaboration</h3>
    <p>Lorem ipsum dolor sit amet, consectetur adipiscing elit sed do eiusmod tempor incididunt ut labore et dolore magna aliqua. Ut enim ad minim v eniam quis nostrud</p>
  </div>
</section>

<section class="future">
  <div class="future-panel">
    <h2>INVESTING FOR<br>THE FUTURE</h2>
    <div class="rule-white"></div>
    <p>Lorem ipsum dolor sit amet, consectetur adipiscing elit sed do eiusmod tempor incididunt ut labore et dolore magna aliqua. Ut enim ad minim veniam quis nostrud exercitation ullamco laboris &nbsp;nisi ut aliquip ex ea commodo consequat. Duis aute irure dolor in .numquam eius modi tempora incidunt ut labore et dolore magnam aliquam quaerat voluptatem. Ut enim ad minima veniam</p>
    <a class="btn-outline" href="#">READ MORE</a>
  </div>
  <div class="future-photo" role="img" aria-label="Photo of an advisor reviewing market charts on a laptop with a client"></div>
</section>

<footer class="site-footer">
  <div class="footer-brand">Investment company</div>
  <nav class="footer-nav">
    <a href="#">HOME</a><a href="#">ABOUT US</a><a href="#">INVESTMENTS</a><a href="#">INVESTORS</a><a href="#">CONTACT US</a>
  </nav>
  <div class="footer-rule"></div>
  <div class="copyright">Copyright © 2024 All Rights Reserved</div>
</footer>
</body>
</html>
```